User-interface and web design for new forum-style communication platform

We developed a new forum-style communication platform specially targetting stock investors to share and discuss information on companies listed on the stock exchange.

You have complete freedom for designing the user-interface and web design. Designs should include all features listed below.

Please read the attached document for full specifications. Also attached is a mockup of the layout, but this is only directional. A mockup for the user-profile is also attached, but does not need to be designed.

This project focusses on the homepage and thread view.

The winner(s) will be asked to design the complete project. (create thread box, user profile, registering, settings...)

We are looking for a well thought out, smart design that incorporates the specifications in the attached document. Please do not hesitate to contact us if anything is not clear.

Target Market(s)

Stock investors from 25 to 60 years old (the people that are currently on investor forums)

Industry/Entity Type

Communication

Font styles to use
Sans Serif

Colors

Designer to choose colors to be used in the design.

Requirements
Must have
• Full homepage design & Thread view specified in the attached document.
Nice to have
• Create thread view
- Field for adding tags
- field for subject of the thread
- text box with basic text editing
- method for sharing media
Should not have
• Logo design.

```html
<!DOCTYPE html>
<html lang="en">
<head>
<meta charset="utf-8">
<title>Tickerhall – Public conversations</title>
<link href="https://fonts.googleapis.com/css2?family=Lato:ital,wght@0,400;0,700;1,400&display=swap" rel="stylesheet">
<style>
:root{
  --navy:#03597c;
  --navy-dark:#024a68;
  --teal-light:#7ebdc6;
  --cream:#f9f8ea;
  --paper:#f1eedc;
  --sand:#e6dfb4;
  --yellow:#f6cf69;
  --red:#d8401f;
  --text:#333;
  --muted:#5a5a5a;
  --link:#3a6f8c;
  --date:#e0645a;
  --line:#dcdcdc;
  --footer:#f3f4f2;
}
*{box-sizing:border-box;margin:0;padding:0}
html,body{width:1200px;height:997px;overflow:hidden}
body{font-family:'Lato',sans-serif;color:var(--text);background:var(--paper);position:relative;font-size:13px}
.abs{position:absolute}
a{color:inherit;text-decoration:none}

/* header */
.site-header{left:0;top:0;width:1200px;height:81px;background:var(--cream);border-bottom:1px solid #ece8cf}
.site-name{left:133px;top:24px;font-size:28px;font-weight:400;color:var(--navy)}
.search-box{left:335px;top:25px;width:440px;height:34px;background:#fff;border:1px solid #e4dfbf;border-radius:2px}
.search-box svg{position:absolute;left:9px;top:9px}
.search-box .query{position:absolute;left:34px;top:10px;font-size:11px;color:#555}
.btn-save,.btn-clear{position:absolute;top:2px;height:28px;border-radius:3px;color:#fff;font-size:15px;text-align:center;line-height:28px}
.btn-save{left:306px;width:64px;background:var(--navy)}
.btn-clear{left:373px;width:64px;background:var(--teal-light)}
.notify-badge{left:864px;top:19px;width:44px;height:44px;border-radius:50%;background:#f0e5b5;}
.notify-badge span{position:absolute;left:5px;top:5px;width:34px;height:34px;border-radius:50%;background:var(--navy);color:#fff;font-size:19px;text-align:center;line-height:34px}
.notify-tip{left:833px;top:73px;width:105px;height:29px;background:#fff;border:1px solid #e4dfbf;border-radius:2px;font-size:13px;color:var(--navy);text-align:center;line-height:28px}
.user-menu{left:989px;top:27px;width:79px;height:28px;background:var(--navy);border-radius:2px;color:#fff;font-size:13px;line-height:28px;padding-left:12px}
.user-menu i{position:absolute;right:0;top:0;width:22px;height:28px;background:var(--sand)}
.user-menu i svg{position:absolute;left:6px;top:11px}

/* sidebar */
.panel{left:131px;width:281px;background:#f6f6f2;border-radius:2px;box-shadow:0 1px 0 #cfcab0}
.panel-head{height:28px;background:var(--navy);color:#fff;font-size:17px;line-height:27px;padding-left:42px;position:relative;border-radius:2px 2px 0 0}
.panel-head svg{position:absolute;left:10px;top:5px}
.panel-head.muted{background:#426c82}
.user-search{margin:10px 10px 0;height:33px;background:#fff;border:1px solid #ccc;position:relative;font-size:13px;color:#555;line-height:31px;padding-left:9px}
.user-search svg{position:absolute;right:10px;top:6px}
.list{list-style:none;padding:5px 5px 0}
.list li{height:30px;line-height:29px;padding-left:25px;font-size:13.5px;color:var(--link);background:#fff;border-bottom:1px solid #eee;position:relative}
.list li::before{content:"»";position:absolute;left:8px;top:-1px;font-size:14px}
.list li.active{background:#f9f7e8;color:#222}
.show-all{margin-top:10px;height:24px;background:var(--sand);font-size:11px;text-align:right;padding-right:13px;line-height:24px;color:#222}

/* main */
.breadcrumb{left:452px;top:98px;font-size:12.5px;color:#333}
.breadcrumb a{color:var(--link)}
.tabs{left:450px;top:133px;height:28px;width:272px;background:#fff;border-radius:14px;display:flex;font-size:13.5px;color:var(--link)}
.tabs span{line-height:28px;text-align:center;border-right:1px solid #ddd}
.tabs .on{background:var(--yellow);border-radius:14px 0 0 14px;width:79px;color:var(--navy)}
.tabs .t2{width:97px}.tabs .t3{width:96px;border:none}
.tab-drop{left:454px;top:165px;width:77px;height:51px;background:#fff;border:1px solid #e7e3cc;z-index:3;font-size:13.5px;color:var(--navy);text-align:center}
.tab-drop div{height:21px;line-height:21px;margin-top:2px}
.tab-drop .on{background:var(--sand)}
.create-btn{left:944px;top:161px;width:125px;height:28px;background:var(--red);color:#fff;border-radius:2px;font-size:13.5px;font-weight:700;line-height:28px;padding-left:30px}
.create-btn svg{position:absolute;left:9px;top:7px}

.thread{left:450px;width:619px;background:#fff;border:1px solid #ddd;border-radius:2px}
.thread-tag{left:460px;width:95px;height:33px;background:var(--navy);color:#fff;font-size:17px;text-align:center;line-height:32px;border-radius:2px 2px 0 0;z-index:2}
.avatar{width:141px;height:141px;border:1px solid #d4d4d4;padding:3px;background:#fff}
.avatar div{width:100%;height:100%}
.t-title{font-size:18px;color:#3e6a80}
.t-meta{font-size:12.5px;color:var(--muted)}
.t-meta u{color:#444;margin-left:4px}
.t-meta .date{color:var(--date);margin-left:8px}
.t-body{width:436px;font-size:12.2px;line-height:17px;color:#555}
.t-foot{width:436px;border-top:1px solid #e3e3e3;height:1px}
.t-actions{font-size:11.5px;font-weight:700;color:var(--link)}
.t-actions u{color:#333}
.t-actions span{margin-left:18px}
.t-buttons{display:flex;height:22px;background:#eee;font-size:12px;color:#333;line-height:22px}
.t-buttons div{text-align:center}
.t-buttons .reply{width:49px;background:var(--yellow)}
.t-buttons .reply.idle{background:#d8d8d8}
.reply-box{left:450px;top:488px;width:619px;height:86px;border-left:4px solid #d8cf9c}
.reply-avatar{left:463px;top:488px;width:56px;height:56px;background:#fff;border:1px solid #d4d4d4;padding:2px}
.reply-area{left:529px;top:488px;width:540px;height:86px;background:#f4f4f2;border:1px solid #e0e0dc;border-radius:3px;font-size:12px;font-style:italic;color:#666;padding:7px 6px}
.profile-pop{left:483px;top:784px;width:95px;height:52px;background:#fff;border:1px solid #e4e4e4;z-index:3;font-size:13.5px;color:var(--navy);text-align:center}
.profile-pop div{height:20px;line-height:20px;margin-top:2px}
.profile-pop .on{background:var(--sand)}
.to-top{left:1012px;top:910px;width:57px;height:28px;background:#a8b9c4;color:#fff;font-size:12px;font-weight:700;line-height:28px;padding-left:7px;border-radius:2px}
.to-top svg{position:absolute;right:6px;top:9px}
.site-footer{left:0;top:947px;width:1200px;height:50px;background:var(--footer)}
</style>
</head>
<body>

<header class="site-header abs"></header>
<div class="site-name abs">Tickerhall</div>
<div class="search-box abs">
  <svg width="17" height="17" viewBox="0 0 17 17"><circle cx="7" cy="7" r="5" fill="none" stroke="#e0d29b" stroke-width="2.4"/><line x1="10.5" y1="10.5" x2="15" y2="15" stroke="#e0d29b" stroke-width="2.6"/></svg>
  <span class="query">#alderon #veltrix</span>
  <a class="btn-save">Save</a>
  <a class="btn-clear">Clear</a>
</div>
<div class="notify-badge abs"><span>3</span></div>
<div class="notify-tip abs">1 New Follower</div>
<div class="user-menu abs">User<i><svg width="10" height="7" viewBox="0 0 10 7"><path d="M1 1l4 4 4-4" fill="none" stroke="#fff" stroke-width="2"/></svg></i></div>

<!-- sidebar -->
<section class="panel abs" style="top:99px;height:90px">
  <div class="panel-head"><svg width="26" height="18" viewBox="0 0 26 18" fill="#cfe0e8"><circle cx="6" cy="6" r="3.5"/><circle cx="20" cy="6" r="3.5"/><circle cx="13" cy="5" r="4.5"/><path d="M0 17c0-5 3-7 6-7s4 1 4 2v5z M26 17c0-5-3-7-6-7s-4 1-4 2v5z M6 18c0-6 3-8 7-8s7 2 7 8z"/></svg>Users</div>
  <div class="user-search">Search<svg width="20" height="20" viewBox="0 0 20 20"><circle cx="8" cy="8" r="6" fill="none" stroke="#555" stroke-width="2.2"/><line x1="12.5" y1="12.5" x2="18" y2="18" stroke="#555" stroke-width="2.6"/></svg></div>
</section>

<section class="panel abs" style="top:208px">
  <div class="panel-head"><svg width="20" height="18" viewBox="0 0 20 18" fill="#cfe0e8"><path d="M1 1h14l-5 6v10l-4-3V7z"/><rect x="15" y="3" width="4" height="2"/></svg>Saved Filters</div>
  <ul class="list"><li>Iteam One</li><li class="active">Iteam Two</li><li>Iteam Three</li><li>Iteam Four</li></ul>
  <div class="show-all">Show All »</div>
</section>

<section class="panel abs" style="top:414px">
  <div class="panel-head"><svg width="20" height="18" viewBox="0 0 20 18" fill="#cfe0e8"><path d="M1 1h8l9 9-7 7-9-9z"/><circle cx="5" cy="5" r="1.6" fill="#03597c"/></svg>Popular Tage</div>
  <ul class="list"><li>Iteam One</li><li class="active">Iteam Two</li><li>Iteam Three</li><li>Iteam Four</li></ul>
  <div class="show-all">Show All »</div>
</section>

<section class="panel abs" style="top:621px">
  <div class="panel-head muted"><svg width="20" height="19" viewBox="0 0 20 19" fill="#cfe0e8"><path d="M10 1l2.6 6 6.4.5-4.9 4.2 1.5 6.3L10 14.6 4.4 18l1.5-6.3L1 7.5 7.4 7z"/></svg>Popular Contributors</div>
  <ul class="list"><li>Iteam One</li><li class="active">Iteam Two</li><li>Iteam Three</li><li>Iteam Four</li></ul>
  <div class="show-all">Show All »</div>
</section>

<!-- main -->
<nav class="breadcrumb abs"><a>Home</a> <a>» Conversations</a> » Public #alderon#veltrix</nav>
<div class="tabs abs"><span class="on">Public</span><span class="t2">Following</span><span class="t3">Contacts</span></div>
<div class="tab-drop abs"><div class="on">Recent</div><div>Popular</div></div>
<a class="create-btn abs"><svg width="16" height="16" viewBox="0 0 16 16" fill="#fff"><path d="M2 11l8-8 3 3-8 8H2z"/><path d="M11 2l1.5-1.5 3 3L14 5z"/></svg>Create Thread</a>

<!-- thread 1 -->
<div class="thread-tag abs" style="top:200px">Thead #1</div>
<article class="thread abs" style="top:209px;height:269px"></article>
<div class="avatar abs" style="left:460px;top:242px"><div role="img" aria-label="Profile photo of the thread author" style="background:linear-gradient(160deg,#dbe6f0,#b9cde0)"></div></div>
<h2 class="t-title abs" style="left:622px;top:240px;font-weight:400">Lorem ipsum dolor sit ametc</h2>
<p class="t-meta abs" style="left:622px;top:269px">Posted by: <u>Martin Hale</u> on <span class="date">31/3/2014 - 2:50</span></p>
<p class="t-body abs" style="left:622px;top:301px">Lorem ipsum dolor sit amet, consectetuer adipiscing elit, sed diam nonummy nibh euismod tincidunt ut laoreet dolore magna aliquam erat volutpat. Ut wisi enim ad minim veniam, quis nostrud exerci tation ullamcorper suscipit lobortisal commodo consequat. Duis autem vel eum iriure dolor in hendrerit in vulputate velit molestie consequat, vel illum dolore eu feugiat nulla facilisis at vero eros et accumsan et iusto odio dignissim qui blandit praesent luptatum zzril delenit augue duis dolore te feugait nulla facilisi.</p>
<div class="t-foot abs" style="left:622px;top:428px"></div>
<div class="t-actions abs" style="left:622px;top:439px"><u>Read more</u><span>12 replies</span><span style="margin-left:11px">250 views</span></div>
<div class="t-buttons abs" style="left:885px;top:436px;width:173px"><div class="reply">Reply</div><div style="width:52px">Share</div><div style="width:72px">Favourite</div></div>

<div class="reply-box abs"></div>
<div class="reply-avatar abs"><svg width="50" height="50" viewBox="0 0 50 50" role="img" aria-label="Default user avatar"><circle cx="25" cy="17" r="10" fill="#5a86ad"/><path d="M5 50c0-14 8-20 20-20s20 6 20 20z" fill="#5a86ad"/><path d="M25 31l-3 4 3 10 3-10z" fill="#fff"/></svg></div>
<div class="reply-area abs">Type your reply here...</div>

<!-- thread 2 -->
<div class="thread-tag abs" style="top:613px">Thead #2</div>
<article class="thread abs" style="top:623px;height:268px"></article>
<div class="avatar abs" style="left:460px;top:655px"><div role="img" aria-label="Profile photo of the thread author" style="background:linear-gradient(180deg,#c9cfd4,#8f979e)"></div></div>
<div class="profile-pop abs"><div class="on">View profile</div><div>View all posts</div></div>
<h2 class="t-title abs" style="left:622px;top:653px;font-weight:400">Lorem ipsum dolor sit ametc</h2>
<p class="t-meta abs" style="left:622px;top:682px">Posted by: <u>Martin Hale</u> on <span class="date">31/3/2014 - 2:50</span></p>
<p class="t-body abs" style="left:622px;top:714px">Lorem ipsum dolor sit amet, consectetuer adipiscing elit, sed diam nonummy nibh euismod tincidunt ut laoreet dolore magna aliquam erat volutpat. Ut wisi enim ad minim veniam, quis nostrud exerci tation ullamcorper suscipit lobortisal commodo consequat. Duis autem vel eum iriure dolor in hendrerit in vulputate velit molestie consequat, vel illum dolore eu feugiat nulla facilisis at vero eros et accumsan et iusto odio dignissim qui blandit praesent luptatum zzril delenit augue duis dolore te feugait nulla facilisi.</p>
<div class="t-foot abs" style="left:622px;top:841px"></div>
<div class="t-actions abs" style="left:622px;top:852px"><u>Read more</u><span>12 replies</span><span style="margin-left:11px">250 views</span></div>
<div class="t-buttons abs" style="left:885px;top:849px;width:173px"><div class="reply idle">Reply</div><div style="width:52px">Share</div><div style="width:72px">Favourite</div></div>

<a class="to-top abs">TOP<svg width="12" height="9" viewBox="0 0 12 9"><path d="M1 7l5-5 5 5" fill="none" stroke="#fff" stroke-width="2.2"/></svg></a>
<footer class="site-footer abs"></footer>
</body>
</html>
```